Diverse, up-scale salon needs eye-catching, unique business cards.

We are looking for a unique business card design for our stylist but that can also be multi functional and used for appointment reminder and referrals. I will need a design in a format that I can modify names and titles going forward. In the past we have had a dark background with the logo on one side, and stylist and contact information on the other but we are open to all ideas. I have included our mission statement as well as branded colors below. The statement doesn't need to go on the card, it's just a reference for target market. We need space for the stylists name, title, instagram handle and then the salons phone number, website and address. I am also open to adding a spot for a qr code linked to the stylist instagram or the salon booking link.

primary brand colors:
#333333 #233415 #36502a #93874a #000000
Mission statement:
Morvane Hair Studio, a high-end salon located in the lively Downtown Farmington, Michigan, is committed to providing exceptional services in a welcoming and relaxed environment to meet the needs of our diverse clientele.
Our salon specializes in contemporary custom haircuts, coloring, extensions, and barbering and beard grooming services. Our team of skilled stylists is passionate and inventive in their hair styling techniques. At the heart of our salon are values centered on quality, innovation, creativity, and above all, comfort. These core values are evident in every appointment across our customizable array of services.
Our goal is to establish a benchmark for exceptional hair care for every human.
Website: www.morvanehairstudio-demo.com
instagram: @morvanehairstudio
address: 41872 Pelton Brook Rd, Farmington MI
phone: 248-316-8847

Industry/Entity Type

Hair Salon

Contact Information for Business Card

Stylist name, title, phone, instagram, website, address, (optional qr code)

Requirements
Should not have
• Does not need mission statement on the card.

```html
<!DOCTYPE html>
<html lang="en">
<head>
<meta charset="utf-8">
<title>Morvane Hair Studio – Business Card</title>
<link href="https://fonts.googleapis.com/css2?family=Open+Sans:wght@700&family=Roboto:wght@300;500&display=swap" rel="stylesheet">
<style>
  :root {
    --stage: #a4a4a4;
    --olive: #958a4b;
    --olive-deep: #877b42;
    --olive-light: #9b9054;
    --ink: #111111;
    --paper: #ffffff;
    --type-light: #f3f1e6;
  }
  * { margin: 0; padding: 0; box-sizing: border-box; }
  html, body {
    width: 1200px;
    height: 1200px;
    overflow: hidden;
    background: var(--stage);
  }
  .canvas {
    position: relative;
    width: 1200px;
    height: 1200px;
  }
  .card {
    position: absolute;
    left: 152px;
    width: 894px;
    height: 524px;
    background: var(--olive);
    overflow: hidden;
    box-shadow: 0 2px 6px rgba(0,0,0,0.25);
  }
  .card--front { top: 50px; }
  .card--back { top: 616px; }
  .card__backdrop {
    position: absolute;
    inset: 0;
    background: linear-gradient(150deg, var(--olive-light) 0%, var(--olive) 45%, var(--olive-deep) 100%);
  }
  .contact-list {
    position: absolute;
    left: 62px;
    top: 328px;
    list-style: none;
  }
  .contact-list__item {
    display: flex;
    align-items: center;
    height: 34.5px;
    font-family: "Roboto", Arial, sans-serif;
    font-weight: 300;
    font-size: 21px;
    color: var(--type-light);
    letter-spacing: 0.2px;
  }
  .contact-list__icon {
    width: 16px;
    height: 16px;
    margin-right: 28px;
    flex: none;
  }
  .brand-mark {
    position: absolute;
    width: 250px;
    height: 250px;
    border-radius: 50%;
    display: flex;
    flex-direction: column;
    align-items: center;
    justify-content: center;
    text-align: center;
  }
  .brand-mark--front {
    left: 583px;
    top: 131px;
    border: 5px solid var(--paper);
  }
  .brand-mark--back {
    left: 322px;
    top: 134px;
    border: 5px solid var(--ink);
  }
  .stylist-name {
    font-family: "Open Sans", Arial, sans-serif;
    font-weight: 700;
    font-size: 29px;
    color: var(--paper);
    white-space: nowrap;
    line-height: 1.1;
  }
  .brand-name {
    font-family: "Roboto", Arial, sans-serif;
    font-weight: 500;
    font-size: 20px;
    letter-spacing: 3px;
    text-transform: uppercase;
    line-height: 1.3;
  }
  .brand-mark--front .brand-name { color: var(--paper); margin-top: 10px; }
  .brand-mark--back .brand-name { color: var(--ink); font-size: 24px; }
</style>
</head>
<body>
<main class="canvas">

  <section class="card card--front" aria-label="Business card front">
    <div class="card__backdrop" role="img" aria-label="Decorative flowing wave artwork in olive and charcoal tones"></div>

    <ul class="contact-list">
      <li class="contact-list__item">
        <svg class="contact-list__icon" viewBox="0 0 16 16" aria-hidden="true"><path d="M3.5 1 L6 1 L7 4.5 L5.3 5.8 C6.2 7.8 8.2 9.8 10.2 10.7 L11.5 9 L15 10 L15 12.5 C15 14 13.8 15 12.5 15 C6.5 14.5 1.5 9.5 1 3.5 C1 2.2 2 1 3.5 1 Z" fill="var(--type-light)"/></svg>
        248-316-8847
      </li>
      <li class="contact-list__item">
        <svg class="contact-list__icon" viewBox="0 0 16 16" aria-hidden="true"><circle cx="8" cy="8" r="6.5" fill="none" stroke="var(--type-light)" stroke-width="1.8"/></svg>
        @morvanehairstudio
      </li>
      <li class="contact-list__item">
        <svg class="contact-list__icon" viewBox="0 0 16 16" aria-hidden="true"><g fill="none" stroke="var(--type-light)" stroke-width="1.4"><circle cx="8" cy="8" r="6.8"/><ellipse cx="8" cy="8" rx="3" ry="6.8"/><path d="M1.2 8 H14.8 M2.3 4.5 H13.7 M2.3 11.5 H13.7"/></g></svg>
        www.morvanehairstudio-demo.com
      </li>
      <li class="contact-list__item">
        <svg class="contact-list__icon" viewBox="0 0 16 16" aria-hidden="true"><path d="M8 15 C5 11 3 8.5 3 6 A5 5 0 0 1 13 6 C13 8.5 11 11 8 15 Z M8 4.3 A1.7 1.7 0 1 0 8 7.7 A1.7 1.7 0 1 0 8 4.3 Z" fill="var(--type-light)" fill-rule="evenodd"/></svg>
        41872 Pelton Brook Rd, Farmington MI
      </li>
    </ul>

    <div class="brand-mark brand-mark--front">
      <p class="stylist-name">Daniel Okafor</p>
      <p class="brand-name">Morvane<br>Hair Studio</p>
    </div>
  </section>

  <section class="card card--back" aria-label="Business card back">
    <div class="brand-mark brand-mark--back">
      <p class="brand-name">Morvane<br>Hair Studio</p>
    </div>
  </section>

</main>
</body>
</html>
```